Willowmere Spa and Beauty Ltd. (Name of business)

I need a business card designed for this new company based out of Toronto Ontario. We specialize in Eyelash Extensions, Manicures and Pedicures, body waxing, massages, laser hair removal and botox treatments. Also offer a variety of products for sale, such as skin cream serums, collagen gel, eye cream, etc. It is a safe relaxing and non-judgemental environnment. Clients are welcome to come be pampered for the half or full day. Many service packages to choose from.

Open 7days per week from 8am to 8pm.

Priscilla Dunmore
Spa Facilitator
Willowmere Spa and Beauty Ltd.
7200 Harcourt St; Suite 1400
Toronto ON K2P 9W4

OFFICE: 416.790.4100
FAX: 416.790.4101
CELL: 416.632.1987
EMAIL: priscilla.dunmore@willowmerespa.com

Target Market(s)

Target market is primarily female ranging from 16 years old to 50 years old.

Industry/Entity Type

Business

Contact Information for Business Card

Priscilla Dunmore
Spa Facilitator
7200 Harcourt St; Suite 1400
Toronto ON K2P 9W4

OFFICE: 416.790.4100
FAX: 416.790.4101
CELL: 416.632.1987

Logo Text

I dont have a logo yet. I would like it simple but sophisticated and modern.

Font styles to use
Serif

Requirements
Must have
• all pertinent details such as company name, logo, name and contact information, services that are offered, including package rates
Nice to have
• Company name and logo prominent. A card that is neat and the information such as address, phone number, fax, email, etc is not too crowded but laid out in an easy to read format.
• Possibly on the back of card - some of the services offered could be listed, as well as professional cream lotions and serums. Hours of operation etc.

```html
<!DOCTYPE html>
<html lang="en">
<head>
<meta charset="utf-8">
<title>Willowmere Spa and Beauty Ltd. – Business Card</title>
<link href="https://fonts.googleapis.com/css2?family=Arimo:wght@400&family=Carlito:ital@0;1&family=Tinos:ital,wght@0,400;1,700&display=swap" rel="stylesheet">
<style>
  :root {
    --paper: #ffffff;
    --ink: #111111;
    --card-edge: #8a8a8a;
  }
  html, body {
    margin: 0;
    padding: 0;
    width: 1200px;
    height: 1200px;
    overflow: hidden;
    background: var(--paper);
  }
  .canvas {
    position: relative;
    width: 1200px;
    height: 1200px;
    color: var(--ink);
    font-family: "Arimo", Arial, sans-serif;
  }
  .side-label {
    position: absolute;
    font-family: "Tinos", "Times New Roman", serif;
    font-size: 22px;
    line-height: 1;
  }
  .side-label--front { left: 67px; top: 250px; }
  .side-label--back { left: 65px; top: 689px; }

  .card {
    position: absolute;
    width: 755px;
    height: 379px;
    border: 1px solid var(--card-edge);
    box-sizing: border-box;
    background: var(--paper);
  }
  .card--front { left: 231px; top: 201px; }
  .card--back { left: 234px; top: 645px; }

  .card > * { position: absolute; margin: 0; line-height: 1; white-space: nowrap; }

  /* Front */
  .brand-mark {
    left: 150px; top: 38px;
    width: 96px; height: 96px;
    border: 5px solid var(--ink);
    border-radius: 50%;
    box-sizing: border-box;
  }
  .brand-name {
    left: 40px; top: 165px;
    width: 350px;
    text-align: center;
    font-size: 32px;
    letter-spacing: 1px;
    line-height: 1.35;
  }
  .front-holder { left: 436px; top: 256px; font-size: 23px; }
  .front-title { left: 463px; top: 291px; font-size: 19px; }

  /* Back */
  .back-mark {
    left: 66px; top: 52px;
    width: 118px; height: 118px;
    border: 6px solid var(--ink);
    border-radius: 50%;
    box-sizing: border-box;
  }
  .company-title {
    left: 250px; top: 22px;
    font-family: "Tinos", "Times New Roman", serif;
    font-style: italic;
    font-weight: 700;
    font-size: 27px;
  }
  .hours {
    left: 245px; top: 60px;
    font-family: "Carlito", Calibri, sans-serif;
    font-size: 23px;
  }
  .back-holder { left: 198px; top: 142px; font-size: 23px; }
  .back-title { left: 226px; top: 178px; font-size: 19px; letter-spacing: 0.5px; }
  .phones {
    right: 18px; top: 217px;
    text-align: right;
    font-size: 20px;
    letter-spacing: 1px;
    line-height: 25px;
  }
  .address {
    left: 43px; top: 290px;
    font-size: 20px;
    letter-spacing: 1px;
    line-height: 25px;
    font-style: normal;
  }
  .email {
    left: 43px; top: 339px;
    font-family: "Carlito", Calibri, sans-serif;
    font-style: italic;
    font-size: 23px;
  }
</style>
</head>
<body>
<main class="canvas">
  <p class="side-label side-label--front">Front</p>
  <section class="card card--front" aria-label="Card front">
    <span class="brand-mark" aria-hidden="true"></span>
    <h1 class="brand-name">WILLOWMERE SPA<br>AND BEAUTY LTD</h1>
    <p class="front-holder">Priscilla Dunmore</p>
    <p class="front-title">Spa Facilitator</p>
  </section>

  <p class="side-label side-label--back">Back</p>
  <section class="card card--back" aria-label="Card back">
    <span class="back-mark" aria-hidden="true"></span>
    <h2 class="company-title">Willowmere Spa and Beauty Ltd.</h2>
    <p class="hours">Open 7days per week from 8am to 8pm.</p>
    <p class="back-holder">Priscilla Dunmore</p>
    <p class="back-title">Spa Facilitator</p>
    <p class="phones">OFFICE: 416.790.4100<br>FAX: 416.790.4101<br>CELL: 416.632.1987</p>
    <address class="address">7200 Harcourt St; Suite 1400<br>Toronto ON K2P 9W4</address>
    <p class="email">EMAIL: priscilla.dunmore@willowmerespa.com</p>
  </section>
</main>
</body>
</html>
```